【 概要 】 司法書士が法律過疎地域に赴き、法律相談会を実施します。 【 依頼内容 】※基本的には添付資料をご確認ください。 ・サイズ:A4 両面 ・ページ数:2ページ ・素材の用意(画像・文章等):相談して決めたいです 【 デザインイメージ 】 ・ターゲット層:全年代ですがご年配の方にもわかりやすく。 ・雰囲気:シンプル、親しみやすい。 【 契約金額(税抜) 】 3万円 ※契約金額(税込)からシステム利用料を差し引いた金額が、ワーカーさまの受取金額となります その他ご質問等ありましたら、気軽にお問い合わせください。 ご応募をお待ちしております! |

```html
<!DOCTYPE html>
<html lang="ja">
<head>
<meta charset="utf-8">
<title>司法書士 無料法律相談会</title>
<link href="https://fonts.googleapis.com/css2?family=M+PLUS+Rounded+1c:wght@500;700;800&family=Noto+Sans+JP:wght@400;500;700;900&display=swap" rel="stylesheet">
<style>
:root{
  --navy:#1f3c72;
  --yellow:#fbe38a;
  --yellow-soft:#fdf1c4;
  --orange:#f0882b;
  --teal:#27b0ae;
  --green:#5cb244;
  --grey:#8c8c8c;
  --red:#e2412f;
  --blue:#2b8fd6;
  --ink:#2a2a2a;
}
*{box-sizing:border-box;margin:0;padding:0}
html,body{width:848px;height:1200px;overflow:hidden;background:#fff}
body{font-family:"Noto Sans JP",sans-serif;color:var(--ink);position:relative}
.round{font-family:"M PLUS Rounded 1c",sans-serif}

.hero{position:absolute;left:0;top:0;width:848px;height:215px;background:var(--yellow)}
.hero-figure{position:absolute;left:28px;top:18px;width:150px;height:190px;border-radius:70px 70px 10px 10px;background:linear-gradient(#f6f0e4,#e9d6a8)}
.headline{position:absolute;left:215px;top:22px;font-weight:800;font-size:33px;line-height:1.4;color:var(--navy)}
.badges{position:absolute;left:215px;top:118px;display:flex;gap:14px}
.badge{height:76px;border-radius:12px;color:#fff;font-weight:800;display:flex;align-items:center;justify-content:center;text-align:center;line-height:1.15}
.badge.free-booking{width:170px;background:var(--orange);font-size:30px}
.badge.free-fee{width:170px;background:var(--teal);font-size:30px}
.badge.pair{width:170px;background:var(--green);font-size:25px}

.band{position:absolute;left:0;top:226px;width:848px;height:44px;background:var(--navy);color:#fff;font-weight:800;font-size:26px;text-align:center;line-height:44px}

.topics{position:absolute;left:26px;top:282px;width:796px;display:grid;grid-template-columns:repeat(3,1fr);gap:10px 14px}
.topic{border:2px solid var(--grey);border-radius:8px;overflow:hidden;height:122px;background:#fff}
.topic h3{background:var(--grey);color:#fff;font-size:16px;font-weight:700;text-align:center;height:28px;line-height:28px}
.topic h3.small{font-size:12.5px}
.topic p{padding:6px 8px;font-size:14px;line-height:1.32;text-align:center;font-weight:500}
.topic .note{display:block;font-size:9px;line-height:1.3;padding:0;margin-top:1px}

.standing{position:absolute;left:0;top:540px;width:848px;height:112px;background:var(--yellow-soft)}
.standing-figure{position:absolute;left:28px;top:6px;width:100px;height:106px;border-radius:50px 50px 6px 6px;background:linear-gradient(#f6f0e4,#e9d6a8)}
.standing h2{position:absolute;left:140px;top:14px;font-size:40px;font-weight:800;color:var(--navy);line-height:1.05}
.standing h2 small{display:block;font-size:22px}
.fields{position:absolute;left:480px;top:10px;display:flex;gap:10px}
.field{width:76px;height:76px;border-radius:50%;background:var(--navy);color:#fff;font-weight:800;font-size:17px;display:flex;align-items:center;justify-content:center;text-align:center;line-height:1.15}
.field.other{background:#6b7fa6}
.standing .caution{position:absolute;left:480px;top:90px;font-size:12px;color:var(--red);font-weight:500}

.venues{position:absolute;left:26px;top:668px;width:796px;display:flex;gap:16px}
.venue{flex:1;border:4px solid var(--orange);border-radius:14px;padding:14px 16px;height:330px;background:#fff}
.venue.east{border-color:var(--blue)}
.venue h3{font-size:27px;font-weight:900;color:var(--navy);border-bottom:2px solid #ccc;padding-bottom:4px}
.venue .addr{font-size:13px;margin-top:4px}
.schedule{display:flex;align-items:center;gap:10px;margin-top:14px}
.day{font-size:27px;font-weight:900;color:var(--navy)}
.time{background:var(--navy);color:#fff;font-size:22px;font-weight:700;padding:2px 10px;border-radius:4px}
.venue .sub{font-size:11px;margin-top:4px;color:#555}
.booking{margin-top:20px;display:flex;align-items:center;gap:10px}
.booking-tag{writing-mode:vertical-rl;background:var(--red);color:#fff;font-weight:700;font-size:14px;padding:8px 4px;border-radius:4px}
.booking-body .org{font-size:14px;font-weight:700}
.phone{display:flex;align-items:center;gap:6px;font-size:30px;font-weight:900;color:var(--red);margin-top:4px}
.phone svg{width:28px;height:28px}
.box-note{margin-top:14px;display:flex;gap:8px}
.chip{background:var(--red);color:#fff;font-size:13px;font-weight:700;padding:4px 10px;border-radius:4px;line-height:1.3}
.chip.navy{background:var(--navy)}

.credits{position:absolute;left:26px;top:1060px;width:796px;font-size:13.5px;line-height:1.7}
.credits dt{font-weight:900;color:var(--navy);float:left;width:70px}
.credits dd{margin-left:70px}
</style>
</head>
<body>

<header class="hero">
  <div class="hero-figure" role="img" aria-label="笑顔で案内する司法書士のイラスト"></div>
  <h1 class="headline round">司法書士は、地域社会に密着し、<br>あなたの財産と権利を守ります</h1>
  <div class="badges round">
    <div class="badge free-booking">予約不要</div>
    <div class="badge free-fee">相談料<br>不要</div>
    <div class="badge pair">２名１組<br>での面談</div>
  </div>
</header>

<div class="band round">こんな時にご相談ください</div>

<section class="topics">
  <div class="topic"><h3>不動産登記</h3><p>売買、贈与、相続による<br>名義変更<br>ローン完済に伴う<br>抵当権抹消等</p></div>
  <div class="topic"><h3>商業・法人登記</h3><p>設立・役員変更<br>増資・商号変更等</p></div>
  <div class="topic"><h3>供託手続</h3><p>地代・家賃について<br>争いがある場合<br>債権者が不明な場合等</p></div>
  <div class="topic"><h3>成年後見制度</h3><p>高齢になりお金の管理に<br>不安がある<br>障害をもつ子の将来<br>について</p></div>
  <div class="topic"><h3 class="small">相続手続・裁判所提出書類作成</h3><p>遺言書作成・相続放棄<br>申述書作成<br>遺産分割調停申立・<br>特別代理人選任申立</p></div>
  <div class="topic"><h3 class="small">簡易裁判所における訴訟代理</h3><p>売買代金や請負代金の<br>請求等<br>裁判外での和解交渉<span class="note">（ただし簡易裁判所の訴額140万円以下）</span></p></div>
</section>

<section class="standing">
  <div class="standing-figure" role="img" aria-label="案内する相談員のイラスト"></div>
  <h2 class="round">常設相談会<small>も開催しております</small></h2>
  <div class="fields round">
    <div class="field">登記</div>
    <div class="field">債務<br>整理</div>
    <div class="field">成年<br>後見</div>
    <div class="field other">その他</div>
  </div>
  <p class="caution">※相談の際には、事前に電話予約が必要です。</p>
</section>

<section class="venues">
  <article class="venue">
    <h3>山辺市民センター</h3>
    <p class="addr">緑野県山辺市東町1-2-3</p>
    <div class="schedule"><span class="day">第３土曜日</span><span class="time">13:30−16:00</span></div>
    <p class="sub">※祝日・年末年始は休み</p>
    <div class="booking">
      <span class="booking-tag">ご予約</span>
      <div class="booking-body">
        <p class="org">緑野県司法書士会やまべ支部</p>
        <p class="phone"><svg viewBox="0 0 24 24"><circle cx="12" cy="12" r="12" fill="#e2412f"/><path d="M8 6c1 0 2 2 2 3s-1 1-1 2 2 3 3 3 1-1 2-1 3 1 3 2-1 2-2 2C11 17 7 13 7 8c0-1 0-2 1-2z" fill="#fff"/></svg>012-345-6789</p>
      </div>
    </div>
    <div class="box-note"><span class="chip">予約受付 前日12時まで</span><span class="chip navy">先着12名</span></div>
  </article>
  <article class="venue east">
    <h3>川東市民福祉センター</h3>
    <p class="addr">緑野県川東市本町45</p>
    <div class="schedule"><span class="day">毎週土曜日</span><span class="time">13:30−16:30</span></div>
    <p class="sub">※祝日・年末年始は休み</p>
    <div class="booking">
      <span class="booking-tag">ご予約</span>
      <div class="booking-body">
        <p class="org">緑野県司法書士会川東支部</p>
        <p class="phone"><svg viewBox="0 0 24 24"><circle cx="12" cy="12" r="12" fill="#e2412f"/><path d="M8 6c1 0 2 2 2 3s-1 1-1 2 2 3 3 3 1-1 2-1 3 1 3 2-1 2-2 2C11 17 7 13 7 8c0-1 0-2 1-2z" fill="#fff"/></svg>0123-45-6780</p>
      </div>
    </div>
    <div class="box-note"><span class="chip">平日 9時〜17時</span></div>
  </article>
</section>

<dl class="credits">
  <dt>共催 ▶</dt>
  <dd>緑野県青年司法書士会　緑野県司法書士会　中央地区司法書士会連合会</dd>
  <dt>後援 ▶</dt>
  <dd>一般社団法人くらし後見サポート緑野支部　緑野県青年土地家屋調査士会<br>中央青年税理士連盟緑野県支部　若葉町　山辺市</dd>
</dl>

</body>
</html>
```